Custom Truck shop New Business Card design

double sided business card including my new logo, brand colors and picking a font I attached, clean and modern look. I attached the old card for some reference. and would like to include the picture of the white truck attached. I would also like to have it with one of my employees info as well. (same info except name and title Brin Tolvay Service Writer)

Dale Porvick
Owner

address
48310 E Calloway Ridge Rd S
STE 217
Marsh Hollow, CO 80219

phone 720-555-0184

email dale@brokenspurrigs.example

website brokenspurrgis.example

social @brokenspurrigs

Target Market(s)

men 18-60

Industry/Entity Type

Automotive

Contact Information for Business Card

Dale Porvick Owner address 48310 E Calloway Ridge Rd S STE 217 Marsh Hollow, CO 80219 phone 720-555-0184 email dale@brokenspurrigs.example website brokenspurrgis.example social @brokenspurrigs

Font styles to use
Other font styles liked:
• fonts attached

Requirements
Must have
• new logo, orange #FC68D, Charcoal #333333
Nice to have
• the white truck

```html
<!DOCTYPE html>
<html lang="en">
<head>
<meta charset="utf-8">
<title>Broken Spur Rigs — Business Card</title>
<link href="https://fonts.googleapis.com/css2?family=Archivo:ital,wght@1,900&family=Outfit:wght@400;500;600&display=swap" rel="stylesheet">
<style>
  :root {
    --orange: #fc6a2d;
    --charcoal: #333333;
    --paper: #ffffff;
    --backdrop: #ececee;
    --photo-light: #4a4a4a;
    --photo-dark: #262626;
  }
  * { margin: 0; padding: 0; box-sizing: border-box; }
  html, body { width: 1200px; height: 1200px; overflow: hidden; }
  body {
    background: var(--backdrop);
    font-family: "Outfit", sans-serif;
    color: var(--charcoal);
    position: relative;
  }
  .card {
    position: absolute;
    left: 151px;
    width: 899px;
    height: 514px;
    overflow: hidden;
  }
  .card--front { top: 78px; background: var(--paper); }
  .card--back { top: 612px; }

  /* Front: brand block */
  .brand-mark {
    position: absolute;
    left: 205px; top: 95px;
    width: 102px; height: 102px;
    border-radius: 50%;
    background: var(--charcoal);
    border: 5px solid var(--orange);
  }
  .brand-name {
    position: absolute;
    left: 46px; width: 420px; top: 212px;
    text-align: center;
    font-weight: 600;
    font-size: 34px;
    line-height: 1;
    letter-spacing: 1px;
    color: var(--charcoal);
  }
  .social {
    position: absolute;
    left: 156px; width: 200px; top: 325px;
    text-align: center;
  }
  .social__icons { display: flex; justify-content: center; gap: 5px; }
  .social__icon {
    width: 22px; height: 22px;
    border-radius: 3px;
    background: var(--orange);
  }
  .social__handle { margin-top: 6px; font-size: 15px; font-weight: 500; line-height: 1.2; }

  /* Front: person block */
  .person { position: absolute; left: 546px; top: 145px; }
  .person__name {
    font-family: "Archivo", sans-serif;
    font-style: italic; font-weight: 900;
    font-size: 31px; line-height: 1;
    color: var(--orange);
    text-transform: uppercase;
  }
  .person__title {
    font-family: "Archivo", sans-serif;
    font-style: italic; font-weight: 900;
    font-size: 17px; line-height: 1; margin-top: 4px;
    color: var(--charcoal);
    text-transform: uppercase;
  }
  .contacts {
    position: absolute; left: 546px; top: 231px;
    list-style: none;
  }
  .contacts__item {
    display: flex; align-items: center;
    height: 22px; margin-bottom: 13px;
    font-size: 16px; font-weight: 500;
  }
  .contacts__icon { width: 20px; height: 20px; margin-right: 15px; flex: none; }

  .address-band {
    position: absolute; left: 0; right: 0; bottom: 0;
    height: 48px;
    background: var(--orange);
    color: var(--paper);
    display: flex; align-items: center; justify-content: center;
    font-size: 15px; font-weight: 500;
  }

  /* Back */
  .truck-photo {
    position: absolute; inset: 0;
    background: radial-gradient(ellipse at 55% 45%, var(--photo-light), var(--photo-dark));
  }
  .back-emblem {
    position: absolute;
    left: 322px; top: 127px;
    width: 262px; height: 262px;
    border-radius: 50%;
    background: var(--paper);
    border: 10px solid var(--orange);
    box-shadow: inset 0 0 0 5px var(--charcoal);
    display: flex; align-items: center; justify-content: center;
    text-align: center;
  }
  .back-emblem__name {
    font-weight: 600;
    font-size: 30px; line-height: 1.15;
    letter-spacing: 1px;
    color: var(--charcoal);
  }
</style>
</head>
<body>
  <section class="card card--front">
    <div class="brand-mark"></div>
    <div class="brand-name">BROKEN SPUR RIGS</div>

    <div class="social">
      <div class="social__icons">
        <span class="social__icon"></span>
        <span class="social__icon"></span>
        <span class="social__icon"></span>
        <span class="social__icon"></span>
      </div>
      <div class="social__handle">@brokenspurrigs</div>
    </div>

    <div class="person">
      <div class="person__name">Dale Porvick</div>
      <div class="person__title">Owner</div>
    </div>

    <ul class="contacts">
      <li class="contacts__item">
        <svg class="contacts__icon" viewBox="0 0 24 24" fill="none" stroke="#fc6a2d" stroke-width="2" stroke-linejoin="round">
          <path d="M5 3h4l2 5-2.5 1.5a11 11 0 0 0 6 6L16 13l5 2v4a2 2 0 0 1-2 2A16 16 0 0 1 3 5a2 2 0 0 1 2-2z"/>
        </svg>
        720-555-0184
      </li>
      <li class="contacts__item">
        <svg class="contacts__icon" viewBox="0 0 24 24" fill="none" stroke="#fc6a2d" stroke-width="2" stroke-linecap="round">
          <circle cx="12" cy="12" r="4"/>
          <path d="M16 8v5a3 3 0 0 0 6 0v-1a10 10 0 1 0-4 8"/>
        </svg>
        dale@brokenspurrigs.example
      </li>
      <li class="contacts__item">
        <svg class="contacts__icon" viewBox="0 0 24 24" fill="none" stroke="#fc6a2d" stroke-width="1.6">
          <circle cx="12" cy="12" r="10"/>
          <ellipse cx="12" cy="12" rx="4.5" ry="10"/>
          <path d="M2 12h20M4 7h16M4 17h16"/>
        </svg>
        brokenspurrgis.example
      </li>
    </ul>

    <div class="address-band">48310 E Calloway Ridge Rd S, STE 217, Marsh Hollow, CO 80219</div>
  </section>

  <section class="card card--back">
    <div class="truck-photo" role="img" aria-label="Dimmed photo of a lifted white pickup truck parked in a lot with bare trees behind"></div>
    <div class="back-emblem">
      <div class="back-emblem__name">BROKEN<br>SPUR<br>RIGS</div>
    </div>
  </section>
</body>
</html>
```